Business card design needed

We need a business card design for a new micro business based in Melbourne (Australia). Our main service is cleaning and fixing Vertical Blinds as a cheaper alternative than buying new blinds. A smaller part of the business is fitting affordable & temporary alternatives to double glazed windows both for noise abatement and climate control and reduction in energy costs.
We could be dealing with commercial as well as residential customers so we need a quality look. The design needs to reflect our core business of vertical blinds cleaning & maintenance.

Target Market(s)

Not sure yet. These Business Cards are going to be used to test the market

Industry/Entity Type

Residential

Contact Information for Business Card

Morlena Tazwick. Vertical Blinds Cleaning, Maintenance & Temporary Window Insulation Solutions. Ph: 03 7142 5063. Mob: 0471 356 249.

```html
<!DOCTYPE html>
<html lang="en">
<head>
<meta charset="utf-8">
<title>Morlena Tazwick – Business Card</title>
<link rel="stylesheet" href="https://fonts.googleapis.com/css2?family=Arimo:wght@700&family=Tinos:wght@700&family=EB+Garamond:wght@400&display=swap">
<style>
  :root {
    --page: #e6e6e6;
    --card: #ffffff;
    --green: #00a651;
    --white: #ffffff;
    --ink: #1a1a1a;
    --blue: #4a6fb5;
    --orange: #e17d22;
  }
  * { margin: 0; padding: 0; box-sizing: border-box; }
  html, body {
    width: 1200px;
    height: 800px;
    overflow: hidden;
    background: var(--page);
  }
  .business-card {
    position: absolute;
    left: 120px;
    top: 130px;
    width: 960px;
    height: 540px;
    background: var(--card);
    box-shadow: 0 2px 6px rgba(0,0,0,0.15);
    overflow: hidden;
  }
  .card-art {
    position: absolute;
    inset: 0;
    width: 960px;
    height: 540px;
  }
  .owner-name {
    position: absolute;
    left: 57px;
    top: 124px;
    font-family: "Arimo", Arial, sans-serif;
    font-weight: 700;
    font-size: 29px;
    color: var(--green);
    white-space: nowrap;
  }
  .contact-line {
    position: absolute;
    left: 632px;
    font-family: "Tinos", "Times New Roman", serif;
    font-weight: 700;
    font-size: 25px;
    color: var(--white);
    white-space: nowrap;
  }
  .contact-line.landline { top: 110px; }
  .contact-line.mobile { top: 179px; }
  .tagline {
    position: absolute;
    left: 52px;
    top: 340px;
    font-family: "EB Garamond", Garamond, serif;
    font-size: 46px;
    line-height: 64px;
    color: var(--orange);
    white-space: nowrap;
  }
  .tagline .lead { color: var(--blue); }
</style>
</head>
<body>
  <div class="business-card">
    <svg class="card-art" viewBox="0 0 640 360" aria-hidden="true">
      <path class="green-panel" fill="#00a651"
            d="M261 0 H640 V140 L375 210 C338 220 314 204 305 168 Z"/>
      <g class="icon-landline">
        <circle cx="387" cy="83" r="15" fill="#ffffff"/>
        <path d="M395 93 L403 100 L396 90 Z" fill="#ffffff"/>
        <path d="M378 80 C378 75 396 75 396 80 L396 82 L392 82 L391 79 C388 78 386 78 383 79 L382 82 L378 82 Z" fill="#1a1a1a"/>
        <path d="M381 90 L383 83 L391 83 L393 90 Z" fill="#1a1a1a"/>
      </g>
      <g class="icon-mobile">
        <circle cx="387" cy="129" r="15" fill="#ffffff"/>
        <path d="M395 139 L403 146 L396 136 Z" fill="#ffffff"/>
        <rect x="382" y="121" width="9" height="16" rx="1.5" fill="#1a1a1a" transform="rotate(-25 386 129)"/>
        <rect x="383.5" y="123" width="6" height="5" fill="#ffffff" transform="rotate(-25 386 129)"/>
      </g>
    </svg>

    <p class="owner-name">Morlena Tazwick</p>
    <p class="contact-line landline">: 03 7142 5063</p>
    <p class="contact-line mobile">: 0471 356 249</p>

    <p class="tagline"><span class="lead">Vertical Cleaning,</span> Maintenance and<br>Temporary Insulation Solutions for Windows.</p>
  </div>
</body>
</html>
```